Business Cards for Communications Technology Company

We are an innovative software company based in Tropical North Queensland, Australia. We have several brands with a focus on communications software for businesses. We are looking for a business card that is very innovate and creative whilst still remaining professional on a corporate level.

Our internal culture is very progressive and expresses a blend between the clarity of our natural surroundings and the highly technological industry we work in. Our current branding blends a modern minimalist typeface with the desire to push the boundaries in the way we communicate.

This is a corporate level business card for the communications software industry and may possibly also encompass our brands MarNetwork, PelFax, TukMailer and our B2B marketing service—with our companies name being Viresca Partners. Showing other brands on the business card is optional not compulsory.

Technical notes:

-We will attach all logo's and some examples of our corporate branding
- Would be willing to print with various papers, embossed, metallic ink, curved edges etc. in a standard business card size

Sample content:

Rowan Pellick
Senior Account Manager
Phone: 1300 842 916 / +617 4583 2764
Email: r.pellick@viresca.com.au
Web: www.viresca.com.au

Sincerely,
Viresca Partners.

```html
<!DOCTYPE html>
<html lang="en">
<head>
<meta charset="utf-8">
<title>Viresca Partners – Business Card</title>
<link rel="stylesheet" href="https://fonts.googleapis.com/css2?family=Roboto:wght@300;700&display=swap">
<style>
  :root {
    --paper: #ffffff;
    --charcoal: #3a3a3a;
    --leaf: #84ae0a;
    --leaf-shade: #5e7f07;
    --ink-light: #ffffff;
    --steel: #6e7073;
    --steel-light: #9a9c9f;
  }
  html, body {
    margin: 0;
    padding: 0;
    width: 1200px;
    height: 1000px;
    overflow: hidden;
    background: var(--paper);
  }
  .card {
    position: relative;
    width: 1200px;
    height: 1000px;
    font-family: "Roboto", Arial, sans-serif;
  }
  .info-panel {
    position: absolute;
    left: 68px;
    top: 202px;
    width: 575px;
    height: 583px;
    background: var(--charcoal);
    border-bottom-left-radius: 96px;
  }
  .name-band {
    position: absolute;
    left: 102px;
    top: 250px;
    width: 593px;
    height: 126px;
    background: var(--leaf);
    color: var(--ink-light);
    text-align: center;
  }
  .band-fold {
    position: absolute;
    left: 643px;
    top: 376px;
    width: 52px;
    height: 34px;
  }
  .person-name {
    position: absolute;
    left: 0;
    right: 0;
    top: 22px;
    margin: 0;
    padding-left: 0;
    font-weight: 700;
    font-size: 44px;
    line-height: 1;
    transform: translateX(-2px);
  }
  .person-role {
    position: absolute;
    left: 0;
    right: 0;
    top: 66px;
    margin: 0;
    font-weight: 300;
    font-size: 33px;
    line-height: 1;
    letter-spacing: -2.2px;
    transform: translateX(-1px);
  }
  .label {
    position: absolute;
    left: 118px;
    margin: 0;
    color: var(--leaf);
    font-weight: 700;
    font-size: 32px;
    line-height: 1;
  }
  .value {
    position: absolute;
    margin: 0;
    color: var(--ink-light);
    font-weight: 300;
    font-size: 31px;
    line-height: 1;
    letter-spacing: 0.3px;
  }
  .value.right { right: 598px; text-align: right; }
  .value.left { left: 118px; }
  .label.phone { top: 410px; }
  .value.phone-main { top: 452px; }
  .value.phone-intl { top: 494px; }
  .label.email { top: 536px; }
  .value.email { top: 578px; }
  .label.web { top: 660px; }
  .value.web { top: 702px; }

  .brand {
    position: absolute;
    left: 690px;
    top: 300px;
    width: 375px;
    text-align: center;
  }
  .brand-disc {
    display: block;
    width: 264px;
    height: 264px;
    margin: 6px auto 0;
    border-radius: 50%;
    background: var(--steel-light);
  }
  .brand-name {
    margin: 24px 0 0;
    font-family: "Roboto", Arial, sans-serif;
    font-weight: 300;
    font-size: 46px;
    letter-spacing: 1px;
    color: var(--steel);
    line-height: 1.1;
  }
</style>
</head>
<body>
  <main class="card">
    <div class="info-panel"></div>

    <div class="name-band">
      <h1 class="person-name">Rowan Pellick</h1>
      <p class="person-role">SENIOR ACCOUNT MANAGER</p>
    </div>
    <svg class="band-fold" viewBox="0 0 52 34" aria-hidden="true">
      <polygon points="0,0 52,0 0,34" fill="var(--leaf-shade)"/>
    </svg>

    <p class="label phone">PHONE :</p>
    <p class="value right phone-main">1300 842 916</p>
    <p class="value right phone-intl">+617 4583 2764</p>

    <p class="label email">EMAIL :</p>
    <p class="value left email">R.PELLICK@VIRESCA.COM.AU</p>

    <p class="label web">WEB :</p>
    <p class="value right web">WWW.VIRESCA.COM.AU</p>

    <div class="brand">
      <span class="brand-disc"></span>
      <p class="brand-name">Viresca Partners</p>
    </div>
  </main>
</body>
</html>
```